Need a Collateral Template for white papers, one page sales sheets and case studies

I would like a series of templates to be used for:

1. White Papers
2. One page handouts
3. Case Studies

I'm uploading a template we've been using and want to keep the same color scheme. I want a very clean look. You do not have to add any of my copy, as we will use these templates for various sales sheets.

Our logo has green, orange and purple. I do not want to highlight these colors but do want to add the logo.

Reason: I would like to see more designs.

Target Market(s)

B2B, credit unions, banks, mortgage companies

Industry/Entity Type

Sales

Font styles to use
Sans Serif

Colors
3176b5
85cae6

Requirements
Must have
• Clean look, modern. Must be able to edit in Illustrator. Must have a font that everyone has ... no strange fonts that don't show up properly on everyone's computer.
Should not have
• The collateral samples I provided are to show the colors we like and what we've been using. Please feel free to start from scratch but use greys, blues, white, some color is fine.

```html
<!DOCTYPE html>
<html lang="en">
<head>
<meta charset="UTF-8">
<title>Sales Sheet – Let someone else pay for your statements</title>
<link rel="stylesheet" href="https://fonts.googleapis.com/css2?family=Fira+Sans:wght@400;500;600&display=swap">
<style>
  :root {
    --navy: #0b3a68;
    --mid-blue: #1d5f9b;
    --brand-blue: #1d62a6;
    --sky: #5bb2e0;
    --pale-sky: #85cae6;
    --text-grey: #555a5f;
    --rule-grey: #b9bdc1;
    --footer-grey: #6d7278;
    --white: #ffffff;
  }
  * { box-sizing: border-box; margin: 0; padding: 0; }
  html, body { width: 927px; height: 1200px; overflow: hidden; background: var(--white); }
  body { font-family: "Fira Sans", Arial, sans-serif; position: relative; }

  .masthead { position: absolute; left: 0; top: 0; width: 927px; height: 197px; background: var(--navy); }
  .masthead svg { position: absolute; left: 0; top: 0; }
  .category { position: absolute; left: 60px; top: 29px; color: var(--pale-sky); font-size: 12px; font-weight: 600; letter-spacing: 2.2px; text-transform: uppercase; }
  .headline { position: absolute; left: 58px; top: 64px; color: var(--white); font-size: 46px; font-weight: 400; line-height: 50px; letter-spacing: -0.3px; }

  .intro { position: absolute; left: 60px; top: 228px; width: 800px; color: var(--brand-blue); font-size: 19.5px; line-height: 32px; }

  .main-column { position: absolute; left: 60px; top: 392px; width: 490px; color: var(--text-grey); font-size: 13.6px; line-height: 23.5px; }
  .subhead { color: var(--sky); font-size: 17px; font-weight: 600; letter-spacing: 0.6px; text-transform: uppercase; margin-bottom: 4px; }
  .main-column p { margin-bottom: 12px; }
  .point-list { list-style: none; margin-bottom: 12px; }
  .point-list li { padding-left: 14px; text-indent: -14px; margin-bottom: 12px; }
  .point-list li::before { content: "› "; color: var(--brand-blue); font-weight: 600; }
  .point-list strong { color: var(--brand-blue); font-weight: 600; }
  .section + .section { margin-top: 18px; }

  .product-visual { position: absolute; left: 624px; top: 397px; width: 218px; height: 221px; background: linear-gradient(160deg, #f4f6f8 0%, #dde5ee 55%, #c6d3e2 100%); border-radius: 2px; box-shadow: 4px 6px 10px rgba(0,0,0,0.18); }

  .callout { position: absolute; left: 624px; top: 674px; width: 303px; height: 334px; border-left: 1px solid var(--pale-sky); border-bottom: 1px solid var(--pale-sky); }
  .callout-notch { position: absolute; left: 0; top: 0; }
  .callout p { position: absolute; left: 24px; top: 22px; width: 200px; color: var(--brand-blue); font-size: 14.5px; line-height: 26px; }

  .footer-brand { position: absolute; left: 60px; top: 1092px; }
  .brand-name { display: flex; align-items: center; gap: 12px; color: var(--mid-blue); font-size: 38px; font-weight: 500; letter-spacing: 3px; line-height: 1; }
  .brand-mark { width: 34px; height: 34px; background: var(--mid-blue); }
  .brand-tagline { margin-top: 6px; color: var(--mid-blue); font-size: 11.5px; font-weight: 500; letter-spacing: 0.6px; text-transform: uppercase; }

  .footer-contact { position: absolute; left: 367px; top: 1104px; width: 560px; color: var(--footer-grey); font-size: 12.5px; letter-spacing: 1.6px; }
  .footer-contact .address { text-transform: uppercase; padding-bottom: 10px; border-bottom: 1px solid var(--rule-grey); }
  .footer-contact .reach { padding-top: 8px; letter-spacing: 0.8px; }
  .footer-contact .reach strong { font-weight: 600; }
</style>
</head>
<body>
  <header class="masthead">
    <svg width="927" height="197" viewBox="0 0 927 197" aria-hidden="true">
      <polygon points="753,0 927,0 927,182 753,121" fill="var(--mid-blue)"/>
      <polygon points="753,140 644,197 892,197" fill="var(--pale-sky)"/>
      <polyline points="753,0 753,121" fill="none" stroke="var(--white)" stroke-width="4"/>
      <polyline points="604,197 753,121 927,182" fill="none" stroke="var(--white)" stroke-width="4"/>
    </svg>
    <div class="category">Category here if needed</div>
    <h1 class="headline">Let someone else pay<br>for your statements</h1>
  </header>

  <p class="intro">Intro paragraph here. Lorem ipsum dolor sit amet, consectetuer adipiscing elit, sed diam nonummy nibh euismod tincidunt ut laoreet dolore magna aliquam erat volutpat. Ut wisi enim ad minim veniam, quis nostrud exerci tation ullamcorper suscipit lobortis nisl ut aliquip ex ea commodo consequat.</p>

  <main class="main-column">
    <section class="section">
      <h2 class="subhead">Subhead placed here</h2>
      <p>Lorem ipsum dolor sit amet, consectetuer adipiscing elit, sed diam nonummy nibh euismod tincidunt ut laoreet dolore magna aliquam erat volutpat. Ut wisi enim ad minim veniam, quis nostrud exerci tation ullamcorper suscipit lobortis nisl ut aliquip ex ea commodo consequat.</p>
      <ul class="point-list">
        <li><strong>Duis autem vel eum iriure dolor.</strong> Hendrerit in vulputate velit esse molestie consequat vel illum dolore eu feugiat.</li>
        <li><strong>Nulla facilisis at vero.</strong> Eros et accumsan et iusto odio dignissim qui blandit praesent luptatum zzril delenit augue duis dolore te feugait.</li>
      </ul>
      <p>Ut wisi enim ad minim veniam, quis nostrud exerci tation ullamcorper suscipit lobortis nisl ut aliquip ex ea commodo consequat. Duis autem vel eum iriure dolor in hendrerit in vulputate velit esse molestie consequat, vel illum dolore eu feugiat nulla facilisis at vero eros et.</p>
    </section>
    <section class="section">
      <h2 class="subhead">Subhead placed here</h2>
      <p>Accumsan et iusto odio dignissim qui blandit praesent luptatum zzril delenit augue duis dolore te feugait nulla facilisi. Lorem ipsum dolor sit amet, consectetuer adipiscing elit, sed diam nonummy nibh euismod tincidunt ut laoreet dolore magna aliquam erat volutpat.</p>
      <p>Duis autem vel eum iriure dolor in hendrerit in vulputate velit esse molestie consequat, vel illum dolore eu feugiat nulla facilisis at vero eros et accumsan et iusto odio dignissim qui blandit praesent luptatum zzril delenit augue duis dolore te feugait nulla faci enim ad minim.</p>
    </section>
  </main>

  <div class="product-visual" role="img" aria-label="Sample printed statements and sponsored inserts fanned out"></div>

  <aside class="callout">
    <svg class="callout-notch" width="26" height="14" viewBox="0 0 26 14" aria-hidden="true">
      <polygon points="0,0 26,0 13,13" fill="var(--pale-sky)"/>
    </svg>
    <p>Callout placed here. Lorem ipsum dolor sit amet, consectetuer adipiscing elit, sed diam nonummy nibh euismod tincidunt ut laoreet dolore magna aliquam erat volutpat. Ut wisi enim ad minim veniam, quis nostrud exerci tation ullamcorper suscipit lobortis nisl ut aliquip ex ea commodo consequat.</p>
  </aside>

  <footer>
    <div class="footer-brand">
      <div class="brand-name"><span class="brand-mark"></span>CORVELLA</div>
      <div class="brand-tagline">Clear Documents, Delivered Well</div>
    </div>
    <div class="footer-contact">
      <div class="address">Corvella Ltd &nbsp;|&nbsp; 48 Harlow Lane, Suite 210 &nbsp;|&nbsp; Brookfield, TX 75200</div>
      <div class="reach"><strong>www.corvella-docs.com</strong> &nbsp;|&nbsp; 555.310.2840</div>
    </div>
  </footer>
</body>
</html>
```